Ember Ridge Clearing postcard ( for direct mailing) and business card design

Design postcards/Business cards
Dale Horvick
Ember Ridge Clearing
482 Copperfern Rd Lewisville,NC 27023
(336) 555-0184 Dale@Emberridgeclearing.example

The postcard will be used for direct mailing to land owners and contractors to advertise our service. Pictures of the process and equipment along with a short summary of what we do. Business card should be contact info and logo.
Updates

The post cards could say something like this: Forestry Mulching machines are capable of clearing land of unwanted trees and brush with limited disturbance to soils or desirable vegetation. Traditional land clearing methods often present an increased risk of erosion by pushing over trees, uprooting the stump and roots, and substantially disturbing soils.In contrast, mulching the vegetation leaves the soil structure intact. The mulched material can be left on the ground and will act as an erosion barrier while returning nutrients back into the soil through decomposition. Over time, grass will naturally grow through the mulch and can be maintained with mowing.

Target Market(s)

Land owners and contractors who need vegetation cleared

Industry/Entity Type

Forestry Mulching

Requirements
Must have
• picture, brief description of service offered, contact info on postcard. Business card should have contact info and logo.
Nice to have
• I like contour lines as a background but I'd like to see other ideas.

```html
<!DOCTYPE html>
<html lang="en">
<head>
<meta charset="utf-8">
<title>Ember Ridge Clearing Postcard</title>
<link rel="stylesheet" href="https://fonts.googleapis.com/css2?family=Arimo:wght@400;700&display=swap">
<style>
  :root {
    --forest: #1d6b35;
    --leaf: #3fae3a;
    --ink: #1b1b1b;
    --paper: #ffffff;
    --rule: #8a8a8a;
    --backdrop: #e4e4e4;
    --photo-a: #6f7a86;
    --photo-b: #c9572c;
  }
  html, body {
    margin: 0;
    width: 908px;
    height: 1200px;
    overflow: hidden;
    background: var(--backdrop);
    font-family: "Arimo", Arial, sans-serif;
  }
  .sheet {
    position: relative;
    width: 908px;
    height: 1200px;
  }
  .card {
    position: absolute;
    left: 194px;
    width: 520px;
    height: 520px;
    background: var(--paper);
    box-shadow: 0 6px 18px rgba(0,0,0,0.18);
  }
  .card--front { top: 50px; }
  .card--back { top: 630px; }
  .card svg { display: block; width: 520px; height: 520px; }
  .brand-name { font-family: "Arimo", Arial, sans-serif; font-weight: 700; fill: var(--ink); letter-spacing: 0.6px; }
  .contact { font-family: "Arimo", Arial, sans-serif; fill: var(--paper); font-size: 8.6px; }
  .service-copy { font-family: "Arimo", Arial, sans-serif; fill: var(--paper); font-size: 8.4px; }
  .address { font-family: "Arimo", Arial, sans-serif; fill: var(--paper); font-size: 8.4px; }
</style>
</head>
<body>
<div class="sheet">

  <!-- Postcard front -->
  <div class="card card--front">
    <svg viewBox="0 0 380 380" xmlns="http://www.w3.org/2000/svg">
      <defs>
        <linearGradient id="photoTone" x1="0" y1="0" x2="1" y2="1">
          <stop offset="0" stop-color="#8c9a8e"/>
          <stop offset="0.45" stop-color="var(--photo-a)"/>
          <stop offset="0.75" stop-color="#9a8f84"/>
          <stop offset="1" stop-color="#5f6468"/>
        </linearGradient>
      </defs>
      <rect width="380" height="380" fill="var(--paper)"/>

      <polygon class="photo" role="img"
        aria-label="Photo of a tracked mulching machine loaded on a trailer, with the owner and two white dogs standing beside it"
        points="0,0 380,124 380,376 0,306" fill="url(#photoTone)"/>

      <polygon class="edge-stripe" points="0,0 380,120 380,130 0,6" fill="var(--leaf)"/>

      <g class="brand" transform="translate(252,22)">
        <rect x="-12" y="4" width="8" height="8" fill="var(--forest)"/>
        <text class="brand-name" x="0" y="12" font-size="12">EMBER</text>
        <text class="brand-name" x="0" y="25" font-size="12">RIDGE</text>
        <text class="brand-name" x="0" y="38" font-size="12">CLEARING</text>
      </g>

      <polygon class="footer-stripe" points="0,300 380,356 380,362 0,306" fill="var(--leaf)"/>
      <polygon class="footer-band" points="0,306 380,362 380,380 0,380" fill="var(--forest)"/>

      <g class="contact-block">
        <g transform="translate(24,335)" fill="var(--leaf)">
          <path d="M0.5 1.5 C2 0 7 0 8.5 1.5 L7.5 3 L6 2.6 L5.8 1.6 C4.8 1.3 4.2 1.3 3.2 1.6 L3 2.6 L1.5 3 Z M1.5 3.6 H7.5 L8 6.5 H1 Z"/>
        </g>
        <text class="contact" x="45" y="342">(336) 555-0184</text>
        <g transform="translate(24,348)">
          <rect x="0" y="0" width="8.5" height="6" fill="var(--leaf)"/>
          <path d="M0 0 L4.25 3.4 L8.5 0" stroke="var(--forest)" stroke-width="0.9" fill="none"/>
        </g>
        <text class="contact" x="45" y="355">Dale@Emberridgeclearing.example</text>
      </g>
    </svg>
  </div>

  <!-- Postcard back -->
  <div class="card card--back">
    <svg viewBox="0 0 380 380" xmlns="http://www.w3.org/2000/svg">
      <rect width="380" height="380" fill="var(--paper)"/>

      <rect class="copy-panel" x="0" y="0" width="172" height="306" fill="var(--forest)"/>
      <g class="service-copy" text-anchor="start">
        <text x="46" y="31">Forestry Mulching is</text>
        <text x="22" y="42" textLength="133">especially economical for</text>
        <text x="22" y="52.5" textLength="133">smaller plots of land or areas</text>
        <text x="22" y="63" textLength="133">with less access. When land</text>
        <text x="22" y="73.5" textLength="133">needs to be cleared for adding</text>
        <text x="22" y="84" textLength="133">roads, servicing pipelines, or</text>
        <text x="22" y="94.5" textLength="133">creating recreational spaces in</text>
        <text x="22" y="105" textLength="133">a wooded area, forestry</text>
        <text x="22" y="115.5" textLength="133">mulching can be a very</text>
        <text x="22" y="126" textLength="133">effective method of clearing</text>
        <text x="22" y="136.5">spaces.</text>

        <text x="46" y="162" textLength="109">Along with making space</text>
        <text x="22" y="172.5" textLength="133">for planned projects, forestry</text>
        <text x="22" y="183" textLength="133">mulching is also a great way to</text>
        <text x="22" y="193.5" textLength="133">clear unwanted vegetation to</text>
        <text x="22" y="204" textLength="133">allow more desirable food</text>
        <text x="22" y="214.5" textLength="133">sources for local wildlife to</text>
        <text x="22" y="225" textLength="133">flourish. Creating access to</text>
        <text x="22" y="235.5" textLength="133">waterways that have become</text>
        <text x="22" y="246" textLength="133">overgrown and clearing space</text>
        <text x="22" y="256.5" textLength="133">for animals to gain new</text>
        <text x="22" y="267" textLength="133">breeding grounds are other</text>
        <text x="22" y="277.5" textLength="133">ways forestry mulching can be</text>
        <text x="22" y="288">helpful.</text>
      </g>

      <g class="address-lines" stroke="var(--rule)" stroke-width="0.8">
        <line x1="190" y1="52" x2="357" y2="52"/>
        <line x1="190" y1="77" x2="357" y2="77"/>
        <line x1="190" y1="102.5" x2="357" y2="102.5"/>
        <line x1="190" y1="128" x2="357" y2="128"/>
        <line x1="190" y1="153.5" x2="357" y2="153.5"/>
        <line x1="190" y1="179" x2="357" y2="179"/>
        <line x1="190" y1="204.5" x2="357" y2="204.5"/>
        <line x1="190" y1="230" x2="357" y2="230"/>
        <line x1="190" y1="255.5" x2="357" y2="255.5"/>
        <line x1="190" y1="281" x2="357" y2="281"/>
        <line x1="190" y1="306" x2="357" y2="306"/>
      </g>

      <g class="brand" transform="translate(42,320)">
        <rect x="-16" y="10" width="8" height="8" fill="var(--forest)"/>
        <text class="brand-name" x="0" y="9" font-size="10">EMBER</text>
        <text class="brand-name" x="0" y="19.5" font-size="10">RIDGE</text>
        <text class="brand-name" x="0" y="30" font-size="10">CLEARING</text>
      </g>

      <rect class="address-band" x="168" y="341" width="212" height="14" fill="var(--forest)"/>
      <text class="address" x="189" y="351">482 Copperfern Rd Lewisville,NC 27023</text>

      <rect class="base-stripe" x="0" y="361" width="380" height="3" fill="var(--leaf)"/>
      <rect class="base-stripe" x="0" y="368" width="380" height="3" fill="var(--leaf)"/>
    </svg>
  </div>

</div>
</body>
</html>
```